Policy Manual in Education

I need the attached document to be put in a publishable format, with graphics a professional layout, and something that looks more like a professional report, etc. Use color samples from http://www.brwt-qx.com/ and www.kv7lo.com, my company is Kv7lo, we were hired to write the report and we also built the BRWT resource center http://www.brwt-qx.com/ .

Target Market(s)

Education

Requirements
Must have
• Look and feel around NM. http://www.brwt-qx.com/ and www.kv7lo.com

```html
<!DOCTYPE html>
<html lang="en">
<head>
<meta charset="utf-8">
<title>BRWT Operational Tools – pages 38–39</title>
<link href="https://fonts.googleapis.com/css2?family=Open+Sans:wght@400;600;700&family=Fira+Sans:ital,wght@1,800&display=swap" rel="stylesheet">
<style>
:root{
  --navy:#0b3a7e;
  --orange:#f39200;
  --ink:#1e1e1e;
  --margin-grey:#e4e4e4;
  --page:#ffffff;
}
*{box-sizing:border-box;margin:0;padding:0}
html,body{width:1200px;height:777px;overflow:hidden;background:var(--margin-grey)}
body{position:relative;font-family:"Open Sans",Arial,sans-serif;color:var(--ink);font-size:11.1px;line-height:15.7px;letter-spacing:-0.1px}
.spread{position:absolute;left:68px;top:0;width:1062px;height:777px;background:var(--page)}
.side-tab{position:absolute;top:0;width:68px;height:777px;display:flex;align-items:center;justify-content:center}
.side-tab.left{left:0}.side-tab.right{right:0;width:70px}
.side-tab span{transform:rotate(-90deg);white-space:nowrap;color:#fff;font-weight:600;font-size:26px;letter-spacing:2px}
.page-head{position:absolute;top:31px;height:5px;background:var(--navy)}
.page-head .brand{position:absolute;left:50%;top:-10px;transform:translateX(-50%);background:var(--page);padding:0 3px;color:var(--orange);font-weight:700;font-size:14px;line-height:16px;letter-spacing:0}
.page-foot{position:absolute;top:739px;height:5px;background:var(--orange)}
.page-foot .num{position:absolute;left:50%;top:-7px;transform:translateX(-50%);background:var(--page);padding:0 10px;color:var(--navy);font-size:12px;line-height:16px}
.block{position:absolute}
.justified{text-align:justify;hyphens:auto;-webkit-hyphens:auto}
ul.bullets{list-style:none}
ul.bullets>li{position:relative;padding-left:12px;margin-bottom:5px;text-align:justify;hyphens:auto;-webkit-hyphens:auto}
ul.bullets>li::before{content:"";position:absolute;left:-9px;top:6px;width:4px;height:4px;background:var(--orange);transform:rotate(45deg)}
ul.sub{list-style:none;margin-top:5px}
ul.sub li{position:relative;padding-left:19px;text-align:justify;hyphens:auto;-webkit-hyphens:auto}
ul.sub li::before{content:"➢";position:absolute;left:2px;top:0;font-size:9px}
.section-title{color:var(--navy);font-weight:700;font-size:12.5px;letter-spacing:0;text-decoration:underline;text-underline-offset:3px}
.banner{position:absolute;left:670px;top:146px;width:441px;height:28px;background:var(--orange);color:#fff;font-family:"Fira Sans",Arial,sans-serif;font-style:italic;font-weight:800;font-size:18px;line-height:28px;padding-left:84px;letter-spacing:0}
.banner b{margin-right:18px}
.prose p{text-indent:34px;text-align:justify;hyphens:auto;-webkit-hyphens:auto;margin-bottom:5px}
.prose sup{font-size:7px}
.cycle{position:absolute;left:895px;top:400px}
</style>
</head>
<body>
<div class="side-tab left"><span>OPERATIONAL TOOLS</span></div>
<div class="side-tab right"><span>OPERATIONAL TOOLS</span></div>
<div class="spread"></div>

<!-- left page -->
<div class="page-head" style="left:90px;width:441px"><span class="brand">QRDEP</span></div>
<div class="page-foot" style="left:90px;width:441px"><span class="num">38</span></div>

<ul class="bullets block" style="left:110px;top:65px;width:420px">
  <li>Work with area business partners to infuse the curricula with real-life business projects.</li>
  <li>Establish workplace experiences with business partners such as mentoring, shadowing, internships, and/or apprenticeships.</li>
</ul>

<h3 class="section-title block" style="left:122px;top:160px">Articulation of credits</h3>
<ul class="bullets block" style="left:110px;top:182px;width:420px">
  <li>Assure that all credits earned by students in BRWTs are transferrable to other public two- and four-year colleges and universities.</li>
  <li>As part of recruitment, outreach, and marketing for the BRWT, share with program stakeholders, parents, and students the high cost savings for college that credit transfer represents.</li>
</ul>

<h3 class="section-title block" style="left:122px;top:292px">Accountability</h3>
<ul class="bullets block" style="left:110px;top:314px;width:420px">
  <li>Develop and implement an evaluation process to determine program effectiveness.</li>
  <li>Establish shared accountability procedures with higher education partners.</li>
  <li>Identify measurable outcomes for your BRWT, such as high-school graduation and dropout rates, attendance rates, college credits earned, certification and associate’s degree completion, admission to four-year institutions, and employment in career or study-related fields.</li>
</ul>

<h3 class="section-title block" style="left:122px;top:461px">Administrative support</h3>
<ul class="bullets block" style="left:110px;top:483px;width:420px">
  <li>Work with the state and local education partners to assure school leaders and educators have professional development opportunities to prepare for the transition to an BRWT.</li>
  <li>Develop and maintain a program of continuing professional development.</li>
  <li>Work with postsecondary partner to establish credentialing programs for BRWT teachers.</li>
</ul>

<h3 class="section-title block" style="left:122px;top:614px">Finance and facilities</h3>
<ul class="bullets block" style="left:110px;top:636px;width:420px">
  <li>Fully understand state funding distributions.</li>
  <li>Establish avenues for coverage of college tuition costs, through the state, the postsecondary institution, and other sources.</li>
</ul>

<!-- right page -->
<div class="page-head" style="left:670px;width:441px"><span class="brand">QRDEP</span></div>
<div class="page-foot" style="left:670px;width:441px"><span class="num">39</span></div>

<ul class="bullets block" style="left:691px;top:66px;width:420px">
  <li>Identify location of BRWT—e.g., current school buildings, college campus, or a stand-alone center.</li>
  <li>Identify sources of funding from local business partners.</li>
</ul>

<h2 class="banner"><b>7.2</b>BRWT Program Toolkit</h2>

<div class="block prose" style="left:670px;top:175px;width:441px">
  <p>The following excerpts from Halvern and Brisco’s High Successful Early College High School Programs, written with support from Kv7lo, provides educators with a better understanding of the complex issues in design, structure, and support systems needed to develop successful BRWT programs<sup>14</sup></p>
  <p>Key features of successful BRWT programs will be presented in the following sections. Taken together, these can serve as a toolkit for you to use as you thoughtfully build and implement your BRWT design. These features, which are interwoven into the tools and recommendations below, include well-defined targeted student populations, clearly defined and measurable outcome goals, strong postsecondary partnerships, rigorous academic standards (including course design, learning outcomes, and sequencing), and a comprehensive student support system. The features of successful BRWT programs begin with the key assumptions of the program.</p>
</div>

<h3 class="section-title block" style="left:703px;top:395px">Assumptions</h3>
<ul class="bullets block" style="left:691px;top:417px;width:202px">
  <li>Key assumptions
    <ul class="sub"><li>BRWT high-school students are in a pipeline toward postsecondary education whether through college enrollment or career education.</li></ul>
  </li>
</ul>
<ul class="bullets block" style="left:691px;top:544px;width:202px">
  <li>Barriers to assumptions
    <ul class="sub"><li>Students can experience obstructions or barriers along this pipeline that could force them out prior to successfully completing the program.</li></ul>
  </li>
</ul>
<ul class="bullets block" style="left:691px;top:649px;width:420px">
  <li>Eliminating barriers
    <ul class="sub"><li>Removal of barriers includes development of well-defined pathways—varying by type, granting institution, and level of credential—for the suc-</li></ul>
  </li>
</ul>

<svg class="cycle" width="220" height="205" viewBox="0 0 220 205" role="img" aria-label="Cycle of assumptions, barriers and pathways">
  <circle cx="110" cy="120" r="83" fill="none" stroke="var(--orange)" stroke-width="7"/>
  <g fill="var(--navy)" stroke="#fff" stroke-width="3">
    <circle cx="110" cy="41" r="37"/>
    <circle cx="110" cy="123" r="38"/>
    <circle cx="39" cy="163" r="34"/>
    <circle cx="180" cy="163" r="34"/>
  </g>
  <g fill="#fff" font-family="Open Sans, Arial, sans-serif" font-size="7.6" text-anchor="middle">
    <text x="110" y="30">Student are in</text><text x="110" y="38">a pipeline to</text><text x="110" y="46">postsecondary</text><text x="110" y="54">education</text>
    <text x="110" y="126">Assumptions</text>
    <text x="39" y="154">Barriers can</text><text x="39" y="162">be removed</text><text x="39" y="170">by welldefined</text><text x="39" y="178">pathways</text>
    <text x="180" y="150">Barriers can</text><text x="180" y="158">impede their</text><text x="180" y="166">completion</text><text x="180" y="174">of the</text><text x="180" y="182">program</text>
  </g>
</svg>
</body>
</html>
```